Banner Design for High End Jewelry Website

We need a banner for our website (brindlestone.com) for a sale that we will be running. The banner should be a size 1187 × 400. I have included a few pieces of jewelry to be included in the banner (do not need to use all, can use just some). The banner should say:
"Christmas is Closer Than You Think Sale!"
Shop Now

Industry/Entity Type

Jewelry

```html
<!DOCTYPE html>
<html lang="en">
<head>
<meta charset="utf-8">
<title>Brindlestone – Fine Estate and Designer Jewelry</title>
<link href="https://fonts.googleapis.com/css2?family=Hind:wght@300;400;600&display=swap" rel="stylesheet">
<style>
:root{
  --brown:#9b7e6b;
  --band:#cdbcab;
  --text:#5a5552;
  --muted:#8a8480;
  --line:#d9d2cc;
  --ribbon:#f3deb5;
  --white:#ffffff;
}
*{box-sizing:border-box;margin:0;padding:0}
html,body{width:1200px;height:854px;overflow:hidden;background:var(--white)}
body{position:relative;font-family:'Hind',sans-serif;color:var(--text)}
.abs{position:absolute}
.utility{top:12px;font-size:16px;letter-spacing:1.5px;display:flex;align-items:center;gap:8px;color:var(--text);font-weight:300}
.utility.small{font-size:12px;letter-spacing:1.4px}
.ribbon{top:0;right:0;width:140px;height:140px}
.brand{left:115px;top:55px;width:322px}
.brand-name{font-size:52px;font-weight:400;color:#111;letter-spacing:1px;line-height:1}
.brand-tag{margin-top:30px;font-size:17px;color:#222;font-weight:400;letter-spacing:.3px}
.search{left:536px;top:66px;width:277px;height:26px;border-bottom:1px solid var(--muted);display:flex;align-items:center}
.search span{font-size:12px;color:var(--text);margin-left:42px}
.search-btn{position:absolute;right:0;top:0;width:27px;height:25px;background:var(--brown);display:flex;align-items:center;justify-content:center}
.tool{top:58px;display:flex;flex-direction:column;align-items:center;gap:6px;font-size:11px;letter-spacing:1.4px;color:var(--text);transform:translateX(-50%)}
.nav{left:457px;top:121px;height:40px;display:flex;gap:2px}
.nav a{background:var(--brown);color:var(--white);text-decoration:none;font-size:15.5px;letter-spacing:1.4px;display:flex;align-items:center;justify-content:center;height:40px}
.hero{left:113px;top:208px;width:974px;height:329px;background:radial-gradient(ellipse at 50% 55%,#fbf8f5 0%,#f1e8e0 55%,#e4d4c6 100%);overflow:hidden}
.hero-piece{position:absolute}
.hero-title{position:absolute;left:0;right:0;top:100px;text-align:center;color:#9a8577;line-height:1}
.hero-title .l1{font-size:50px;font-weight:300}
.hero-title .l2{font-size:50px;font-weight:300;margin-top:6px;display:block}
.hero-title b{font-weight:600}
.hero-cta{position:absolute;left:336px;top:235px;width:207px;height:47px;background:var(--brown);color:var(--white);font-size:33px;font-weight:300;letter-spacing:1px;display:flex;align-items:center;justify-content:center;padding-top:4px}
.arrivals{left:113px;top:572px;width:974px;height:50px;background:var(--band)}
.arrivals h2{text-align:center;color:var(--white);font-weight:300;font-size:24px;letter-spacing:2px;line-height:54px}
.view-all{position:absolute;right:10px;top:9px;width:78px;height:33px;background:var(--brown);color:var(--white);font-size:12px;letter-spacing:1px;display:flex;align-items:center;justify-content:center}
.frame{left:113px;top:622px;width:974px;height:232px;border-left:1px solid var(--line);border-right:1px solid var(--line)}
.product{top:648px;width:288px;text-align:center;font-size:11px;line-height:1.2;color:var(--text)}
.product-img{top:682px;height:172px;width:260px}
.carousel{top:747px;width:18px;height:47px;background:#d8cec6;display:flex;align-items:center;justify-content:center}
</style>
</head>
<body>

<svg class="abs ribbon" viewBox="0 0 140 140" aria-hidden="true">
  <polygon points="0,0 140,0 140,140" fill="var(--ribbon)"/>
  <polygon points="55,0 140,85 140,140 0,0" fill="var(--ribbon)"/>
  <polygon points="104,18 112,24 106,26" fill="#222"/>
  <text x="78" y="32" transform="rotate(45 78 32)" font-family="Hind, sans-serif" font-size="14" fill="#444">Sign up!</text>
</svg>

<div class="abs utility" style="left:584px">
  <svg width="18" height="18" viewBox="0 0 24 24" fill="none" stroke="var(--muted)" stroke-width="1.4"><path d="M5 3h4l2 5-3 2a12 12 0 0 0 6 6l2-3 5 2v4a2 2 0 0 1-2 2A17 17 0 0 1 3 5a2 2 0 0 1 2-2z"/></svg>
  <span>800 - 555 - 0142</span>
</div>
<div class="abs utility" style="left:770px">
  <svg width="16" height="14" viewBox="0 0 24 20" fill="none" stroke="var(--muted)" stroke-width="1.4"><path d="M6 1h12l5 6-11 12L1 7z M1 7h22 M9 1l3 18 3-18"/></svg>
  <span>SELL JEWELRY</span>
</div>
<div class="abs utility small" style="left:939px;top:14px">
  <svg width="18" height="18" viewBox="0 0 24 24" fill="none" stroke="var(--muted)" stroke-width="1.4"><circle cx="12" cy="8" r="5"/><path d="M3 22c1-5 5-7 9-7s8 2 9 7z"/></svg>
  <span style="margin-left:8px">SIGN IN / REGISTER</span>
</div>

<div class="abs brand">
  <div class="brand-name">Brindlestone</div>
  <div class="brand-tag">FINE ESTATE AND DESIGNER JEWELRY</div>
</div>

<div class="abs search">
  <svg style="position:absolute;left:10px;top:3px" width="16" height="16" viewBox="0 0 24 24" fill="none" stroke="var(--muted)" stroke-width="1.6"><circle cx="10" cy="10" r="7"/><path d="M15 15l6 6"/></svg>
  <span>Search</span>
  <div class="search-btn"><svg width="14" height="12" viewBox="0 0 14 12"><path d="M1 6l4 4 8-9" fill="none" stroke="#fff" stroke-width="2.2"/></svg></div>
</div>

<div class="abs tool" style="left:891px">
  <svg width="24" height="18" viewBox="0 0 24 18" fill="none" stroke="var(--muted)" stroke-width="1.3"><rect x="1" y="1" width="22" height="16"/><path d="M1 1l11 9 11-9"/></svg>
  <span>NEWSLETTER</span>
</div>
<div class="abs tool" style="left:984px">
  <svg width="24" height="20" viewBox="0 0 24 22" fill="none" stroke="var(--muted)" stroke-width="1.3"><path d="M12 21S1 14 1 7a5.5 5.5 0 0 1 11-1 5.5 5.5 0 0 1 11 1c0 7-11 14-11 14z"/></svg>
  <span>WISHLIST</span>
</div>
<div class="abs tool" style="left:1062px">
  <svg width="22" height="20" viewBox="0 0 24 22" fill="none" stroke="var(--muted)" stroke-width="1.3"><path d="M1 1h4l3 13h13l2-9H6"/><circle cx="9" cy="19" r="2"/><circle cx="19" cy="19" r="2"/></svg>
  <span>CART (0)</span>
</div>

<nav class="abs nav">
  <a href="#" style="width:145px">FINE JEWELRY</a>
  <a href="#" style="width:129px">TIMEPIECES</a>
  <a href="#" style="width:143px">ACCESSORIES</a>
  <a href="#" style="width:125px">DESIGNERS</a>
  <a href="#" style="width:79px">SALE</a>
</nav>

<section class="abs hero">
  <div class="hero-piece" role="img" aria-label="Gold scale-pattern bangle bracelet set with diamonds" style="left:17px;top:76px;width:183px;height:182px;border-radius:50%;background:radial-gradient(circle at 45% 40%,#e9c66a 0%,#c9973a 60%,rgba(201,151,58,0) 72%)"></div>
  <div class="hero-piece" role="img" aria-label="Gold cocktail ring with sapphire, emerald and ruby cabochons and diamond band" style="left:680px;top:43px;width:257px;height:224px;border-radius:45%;background:radial-gradient(circle at 50% 50%,#4a3a6a 0%,#2f6a5a 35%,#d4a63a 58%,rgba(212,166,58,0) 72%)"></div>
  <div class="hero-title">
    <span class="l1"><b>Christmas</b> is Closer</span>
    <span class="l2">Thank You Think <b>Sale!</b></span>
  </div>
  <div class="hero-cta">SHOP NOW</div>
</section>

<section class="abs arrivals">
  <h2>NEW ARRIVALS</h2>
  <div class="view-all">VIEW ALL</div>
</section>
<div class="abs frame"></div>

<div class="abs product" style="left:135px">Aurelle 6.00 Carat Fancy Diamond 18k Gold Bangle Bracelet</div>
<div class="abs product" style="left:442px">Valenti Coil Diamond Tourmaline 18 Karat Rose Gold Ring</div>
<div class="abs product" style="left:749px">Art Deco Carved Emerald Ruby Diamond Platinum Brooch</div>

<div class="abs product-img" role="img" aria-label="Gold bangle bracelet with fancy brown diamonds" style="left:149px;background:radial-gradient(ellipse at 50% 75%,#b99a5a 0%,#7a6040 25%,rgba(255,255,255,0) 55%)"></div>
<div class="abs product-img" role="img" aria-label="Rose gold coiled ring set with diamonds" style="left:470px;background:radial-gradient(ellipse at 50% 85%,#e0a987 0%,#c98a66 35%,rgba(255,255,255,0) 65%)"></div>
<div class="abs product-img" role="img" aria-label="Art deco platinum brooch with carved emeralds and rubies" style="left:778px;background:radial-gradient(ellipse at 50% 90%,#8a9a8a 0%,#a0506a 25%,#5a8a6a 40%,rgba(255,255,255,0) 65%)"></div>

<div class="abs carousel" style="left:115px"><svg width="8" height="14" viewBox="0 0 8 14"><path d="M7 1L1 7l6 6" fill="none" stroke="#fff" stroke-width="2"/></svg></div>
<div class="abs carousel" style="left:1067px"><svg width="8" height="14" viewBox="0 0 8 14"><path d="M1 1l6 6-6 6" fill="none" stroke="#fff" stroke-width="2"/></svg></div>

</body>
</html>
```